Website Design for NYC Female Attorney – Clean, Warm, Professional

Marian Thorpe, Esq.
www.MarianJThorpeLegal.example

I’m a New York City-based attorney and CPA with a reputation for providing thoughtful, high-integrity legal guidance in both estate planning and small business law. I’ve served over 500 clients, and maintain a perfect 5-star rating. Clients come to me for clarity, compassion, and results — and I want my new website to reflect that.

**🎯 WHAT I NEED:**
A clean, modern, and emotionally resonant website that highlights who I am, what I do, and why clients trust me. It must feel approachable and warm, but still professional and elegant — think Quillo meets boutique law firm. Feminine but not frilly.

**🧩 CORE WEBSITE SECTIONS (Top Navigation):**

1. **Home** – Strong first impression, tagline, CTA (book a call)
Homepage Copy (Sample Layout)
Headline:
Trusted Legal Guidance for Families and Founders.

Subheading:
Whether you’re protecting what you’ve built or building what’s next, I help you navigate estate planning and business law with confidence, compassion, and clarity.

Tagline (beneath logo or footer):
Legal Clarity for Life and Business.
2. **About Marian** – Bio, personal approach, credentials
3. **Services**

* *Estate Planning*
* *Business Law*
4. **Who I Work With** – Ideal clients (parents, entrepreneurs, etc.)
5. **Testimonials** – Client praise and social proof
6. **Success Stories** – Highlighting wins and case types
7. **FAQs** – Warm and clear answers to common questions
8. **Blog** – Thought leadership and helpful tips
8.5 Events
9. **Contact / Book a Call** – Scheduling or contact form

**🖼 STYLE DIRECTION:**

* Clean white backgrounds, soft jewel tones or neutrals
* Professional headshots and personal branding assets available
* Emphasis on readability, trust, and ease of navigation - THIS NEEDS TO BE BUILT OUT SO IT IS TRUSTED BY AI!
* No harsh colors, no corporate/legal clichés (e.g., gavels or scales) - I MEAN THIS. I DO NOT WANT A BORING LAW WEBSITE WITH SCALES AND GAVELS
* Feminine edge (not pink-heavy), with strong hierarchy and callouts

**💡 DESIGN NOTES:**

* Mobile-first design required
* Should include space for video or welcome message
* Easy to update blog or CMS area preferred
* Built in a user-friendly platform like WordPress, Webflow, or similar
* Needs to feel elevated enough to support high-end flat fee packages

**📣 TONE:**
Smart. Warm. Sophisticated. Human.

**⚖️ FINAL DELIVERABLES:**

* Homepage + 5+ interior pages
* Desktop + mobile views
* Style guide (fonts, colors, buttons)
* Bonus if you can help with copy layout/structure (not just visuals)

**📍TARGET AUDIENCE:**

* Busy professionals and families in NYC
* Women and couples who want peace of mind
* Entrepreneurs and creatives needing solid legal support

Here is my current site: www.MarianJThorpeLegal.example
And here is a second business I have: www.QuickCounselDaily.example

Families and business owners

Law

Serif
Sans Serif
Script

• This website must be built to be seen as trustworthy by AI.

```html
<!DOCTYPE html>
<html lang="en">
<head>
<meta charset="utf-8">
<title>Marian Thorpe, Esq. – Estate Planning &amp; Business Law</title>
<link rel="stylesheet" href="https://fonts.googleapis.com/css2?family=Playfair+Display:wght@400;500;600&family=Montserrat:wght@400;500;600;700&display=swap">
<style>
:root{
  --navy:#2d3562;
  --navy-deep:#252c52;
  --pink:#e8318a;
  --pink-soft:#f0438c;
  --ink:#1f2233;
  --muted:#555a6b;
  --mist:#eef0f4;
  --white:#ffffff;
  --footer:#1c1c21;
  --card:#2a3160;
}
*{margin:0;padding:0;box-sizing:border-box}
html,body{width:1200px;height:5310px;overflow:hidden}
body{position:relative;background:var(--white);font-family:"Montserrat",sans-serif;color:var(--ink)}
.abs{position:absolute}
.serif{font-family:"Playfair Display",serif}
.btn{position:absolute;display:flex;align-items:center;justify-content:center;background:var(--pink);color:var(--white);font-size:11px;font-weight:600;letter-spacing:.3px;text-transform:uppercase}
.section-title{position:absolute;left:0;width:1200px;text-align:center;font-family:"Playfair Display",serif;font-weight:500;font-size:40px}
.rule{position:absolute;height:4px;width:76px;background:var(--pink)}
.para{position:absolute;font-size:13.5px;line-height:29px;color:var(--muted)}
/* top bar */
.topbar{left:0;top:0;width:1200px;height:45px;background:var(--navy);color:var(--white);font-size:13px;font-weight:500}
.topbar span{position:absolute;top:13px;display:flex;align-items:center;gap:7px}
.social{position:absolute;width:30px;height:30px;border-radius:50%;background:var(--white)}
/* header */
.header{left:0;top:45px;width:1200px;height:112px;background:var(--white)}
.brand{position:absolute;left:118px;top:28px;width:190px;text-align:center;font-family:"Playfair Display",serif;color:var(--navy)}
.brand small{display:block;font-size:11px;letter-spacing:3px;text-transform:uppercase}
.brand b{display:block;font-weight:500;font-size:21px;letter-spacing:2px;margin-top:6px}
.nav{position:absolute;left:410px;top:49px;display:flex;gap:0;font-size:12.5px;font-weight:600;color:var(--ink)}
.nav a{color:inherit;text-decoration:none;padding:0 12px;border-right:1.5px solid var(--ink);line-height:12px}
.nav a:last-child{border-right:none}
.nav a.active{color:var(--pink);padding-left:0}
/* hero */
.hero{left:0;top:157px;width:1200px;height:561px;background:linear-gradient(100deg,#1a1d2e 0%,#2b2a3a 35%,#5a3a36 60%,#b8744a 75%,#2c2a36 100%)}
.hero-shade{left:0;top:157px;width:1200px;height:561px;background:linear-gradient(90deg,rgba(15,17,30,.75) 0%,rgba(15,17,30,.25) 55%,rgba(15,17,30,0) 100%)}
.hero h1{position:absolute;left:111px;top:292px;font-family:"Playfair Display",serif;font-weight:500;font-size:40px;line-height:54px;color:var(--white)}
.hero-sub{position:absolute;left:111px;top:414px;width:500px;font-size:14.5px;line-height:29px;color:var(--white);font-weight:500}
/* stats */
.stats{left:0;top:718px;width:1200px;height:165px;background:var(--navy)}
.stat{position:absolute;top:40px;color:var(--white)}
.stat .ico{position:absolute;left:0;top:0;width:46px;height:46px;border-radius:50%;background:var(--white)}
.stat h3{position:absolute;left:62px;top:0;font-size:17px;font-weight:600;white-space:nowrap}
.stat p{position:absolute;left:62px;top:28px;width:200px;font-size:13.5px;line-height:25px}
.chev{left:568px;top:856px;width:62px;height:62px;border-radius:50%;background:var(--white);box-shadow:0 4px 12px rgba(0,0,0,.15)}
/* frames & photos */
.frame{position:absolute;border:7px solid var(--pink)}
.photo{position:absolute}
.node{position:absolute;width:58px;height:58px;border-radius:50%;background:var(--navy);border:4px solid var(--white);box-shadow:0 2px 8px rgba(0,0,0,.2)}
/* testimonials */
.testi-card{position:absolute;top:2959px;width:415px;height:241px;background:var(--card);border:1px solid rgba(255,255,255,.35)}
.testi-card .avatar{position:absolute;left:16px;top:24px;width:58px;height:58px;border-radius:50%}
.testi-card .name{position:absolute;left:100px;top:32px;font-family:"Playfair Display",serif;font-size:18px;color:var(--white)}
.testi-card .stars{position:absolute;left:230px;top:32px;color:#ff4b4b;font-size:14px;letter-spacing:4px}
.testi-card .role{position:absolute;left:100px;top:70px;font-size:12.5px;color:var(--white)}
.testi-card .line{position:absolute;left:0;top:98px;width:100%;height:1px;background:rgba(255,255,255,.2)}
.testi-card .quote{position:absolute;left:50px;top:120px;width:320px;font-size:10.5px;line-height:23px;color:rgba(255,255,255,.7)}
.arrow{position:absolute;top:3068px;width:24px;height:24px;border-radius:50%;background:var(--white)}
/* faq */
.faq{position:absolute;left:181px;width:836px;height:60px;background:var(--mist);font-size:14.5px;font-weight:600;color:var(--ink)}
.faq span{position:absolute;left:30px;top:21px}
.faq i{position:absolute;right:22px;top:21px;width:18px;height:18px;border-radius:50%;background:var(--ink)}
.faq i::before,.faq i::after{content:"";position:absolute;left:4px;top:8px;width:10px;height:2px;background:var(--white)}
.faq i::after{transform:rotate(90deg)}
.faq.open{height:124px;background:var(--navy);color:var(--white)}
.faq.open i{background:var(--white)}
.faq.open i::before{background:var(--navy)}
.faq.open i::after{display:none}
.faq.open p{position:absolute;left:30px;top:56px;width:760px;font-size:10.5px;font-weight:400;line-height:22px;color:rgba(255,255,255,.8)}
/* news */
.news-h{position:absolute;font-size:15.5px;font-weight:600;line-height:25px;color:var(--ink)}
.news-p{position:absolute;font-size:12px;line-height:22px;color:var(--muted)}
.news-link{position:absolute;font-size:12px;font-weight:600;color:var(--pink)}
/* footer */
.footer{left:0;top:4809px;width:1200px;height:501px;background:var(--footer)}
.cta-box{left:111px;top:4652px;width:978px;height:324px;background:var(--pink-soft)}
.fnav{position:absolute;left:0;top:5120px;width:1200px;display:flex;justify-content:center;font-size:12.5px;font-weight:600;color:var(--white)}
.fnav a{color:inherit;text-decoration:none;padding:0 18px;border-right:1.5px solid var(--white);line-height:12px}
.fnav a:last-child{border-right:none}
</style>
</head>
<body>

<!-- top bar -->
<div class="abs topbar">
  <span style="left:111px">
    <svg width="12" height="12" viewBox="0 0 24 24"><path fill="#fff" d="M6.6 10.8a15.1 15.1 0 0 0 6.6 6.6l2.2-2.2c.3-.3.7-.4 1-.2 1.1.4 2.3.6 3.6.6.6 0 1 .4 1 1V20c0 .6-.4 1-1 1A17 17 0 0 1 3 4c0-.6.4-1 1-1h3.5c.6 0 1 .4 1 1 0 1.3.2 2.5.6 3.6.1.3 0 .7-.2 1z"/></svg>
    (212) 555-0148</span>
  <span style="left:318px">
    <svg width="13" height="11" viewBox="0 0 24 18"><path fill="#fff" d="M0 0h24v18H0z"/><path fill="none" stroke="#2d3562" stroke-width="2" d="M1 1l11 9 11-9"/></svg>
    marian@marianjthorpelegal.example</span>
  <div class="social" style="left:978px;top:7px" aria-label="Social profile 1"></div>
  <div class="social" style="left:1015px;top:7px" aria-label="Social profile 2"></div>
  <div class="social" style="left:1052px;top:7px" aria-label="Social profile 3"></div>
</div>

<!-- header -->
<header class="abs header">
  <div class="brand"><small>Law Office of</small><b>MARIAN THORPE</b></div>
  <nav class="nav">
    <a class="active" href="#">HOME</a><a href="#">ABOUT</a><a href="#">SERVICES</a><a href="#">WHO I WORK WITH</a><a href="#">RESOURCES</a>
  </nav>
  <div class="btn" style="left:957px;top:35px;width:132px;height:44px;font-size:11.5px">Contact Us</div>
</header>

<!-- hero -->
<section>
  <div class="abs hero" role="img" aria-label="Woman using a tablet by a window overlooking a city at dusk"></div>
  <div class="abs hero-shade"></div>
  <div class="hero">
    <h1>Trusted Legal Guidance for<br>Families &amp; Founders</h1>
    <p class="hero-sub">Whether you're protecting what you've built or building what's next, I help you navigate estate planning and business law with confidence, compassion, and clarity.</p>
  </div>
  <div class="btn" style="left:111px;top:530px;width:134px;height:44px;font-size:11.5px">Book a Call</div>
</section>

<!-- stats -->
<section class="abs stats">
  <div class="stat" style="left:44px"><div class="ico"><svg width="46" height="46"><circle cx="23" cy="23" r="15" fill="none" stroke="#e8318a" stroke-width="2"/><path d="M16 23l5 5 9-10" fill="none" stroke="#2d3562" stroke-width="2.5"/></svg></div><h3>Trusted</h3><p>A trusted advisor to over 500 clients</p></div>
  <div class="stat" style="left:336px"><div class="ico"><svg width="46" height="46"><circle cx="23" cy="23" r="15" fill="none" stroke="#e8318a" stroke-width="2"/><circle cx="23" cy="23" r="7" fill="none" stroke="#2d3562" stroke-width="2"/></svg></div><h3>Dual certified</h3><p>A dual-certified legal financial advisor</p></div>
  <div class="stat" style="left:623px"><div class="ico"><svg width="46" height="46"><circle cx="23" cy="23" r="15" fill="none" stroke="#e8318a" stroke-width="2"/><path d="M23 14l2.6 5.5 6 .7-4.4 4.1 1.2 5.9L23 27.3l-5.4 2.9 1.2-5.9-4.4-4.1 6-.7z" fill="#2d3562"/></svg></div><h3 style="color:var(--pink)">Ratings</h3><p>Proud to be consistently Rated 5 stars</p></div>
  <div class="stat" style="left:928px"><div class="ico"><svg width="46" height="46"><circle cx="23" cy="23" r="15" fill="none" stroke="#e8318a" stroke-width="2"/><circle cx="23" cy="20" r="5" fill="none" stroke="#2d3562" stroke-width="2"/><path d="M15 32c2-5 14-5 16 0" fill="none" stroke="#2d3562" stroke-width="2"/></svg></div><h3>Experienced</h3><p>An experienced estate &amp; business attorney</p></div>
</section>
<div class="abs chev"><svg width="62" height="62"><path d="M25 25l6 5 6-5M25 31l6 5 6-5" fill="none" stroke="#2d3562" stroke-width="2"/></svg></div>

<!-- about -->
<section>
  <div class="frame" style="left:111px;top:1025px;width:361px;height:363px"></div>
  <div class="photo" style="left:134px;top:1054px;width:410px;height:410px;background:linear-gradient(180deg,#8d9cc0 0%,#8393ba 70%,#b9a988 100%)" role="img" aria-label="Portrait of Marian Thorpe seated in a black dress"></div>
  <h2 class="abs serif" style="left:639px;top:1005px;font-size:40px;font-weight:500">About Marian</h2>
  <div class="rule" style="left:639px;top:1065px"></div>
  <p class="para" style="left:639px;top:1088px;width:450px">Lorem ipsum dolor sit amet, consectetur adipiscing elit, sed do eiusmod tempor incididunt ut labore et dolore magna aliqua. Ut enim ad minim veniam, quis nostrud exercitat ion ullamco laboris nisi ut aliquip ex ea commo do consequat. Duis aute irure dolor in reprehenderit in voluptate velit esse cillum dolore eu fugiat nulla pariatur.</p>
  <p class="para" style="left:639px;top:1283px;width:450px">Lorem ipsum dolor sit amet, consectetur adipiscing elit, sed do eiusmod tempor incididunt ut labore et dolore magna aliqua. Ut enim ad minim veniam, quis nostrud exercitat ion ullamco laboris nisi ut aliquip</p>
  <div class="btn" style="left:639px;top:1427px;width:134px;height:42px">Learn More</div>
</section>

<!-- services -->
<section>
  <div class="abs" style="left:0;top:1615px;width:1200px;height:1150px;background:linear-gradient(160deg,#f4f5f8,#e9ebf0 50%,#f1f2f5)"></div>
  <h2 class="section-title" style="top:1700px">Our Services</h2>
  <div class="rule" style="left:562px;top:1762px"></div>

  <h3 class="abs serif" style="left:111px;top:1826px;font-size:25px;font-weight:500">Estate Planning</h3>
  <div class="rule" style="left:111px;top:1866px;width:62px;height:3px"></div>
  <p class="para" style="left:111px;top:1905px;width:450px">Lorem ipsum dolor sit amet, consectetur adipiscing elit, sed do eiusmod tempor incididunt ut labore et dolore magna aliqua. Ut enim ad minim veniam, quis nostrud exercitat ion ullamco laboris nisi ut aliquip ex ea commo do consequat. Duis aute irure dolor in reprehenderit in voluptate velit esse cillum dolore eu fugiat nulla pariatur.</p>
  <div class="btn" style="left:111px;top:2103px;width:134px;height:44px">Learn More</div>

  <div class="frame" style="left:742px;top:1800px;width:345px;height:345px"></div>
  <div class="photo" style="left:670px;top:1825px;width:394px;height:392px;background:linear-gradient(135deg,#1e2b4a 0%,#3a3f52 40%,#b07848 65%,#eaeaea 100%)" role="img" aria-label="Hands passing a house key over a small wooden house model and paperwork"></div>

  <svg class="abs" style="left:590px;top:2120px" width="100" height="450" viewBox="0 0 100 450"><path d="M70 12 C20 12 10 20 10 60 L10 400 C10 435 0 441 -40 441" fill="none" stroke="#2d3562" stroke-width="2" stroke-dasharray="6 5"/></svg>
  <div class="node" style="left:647px;top:2101px"><svg width="50" height="50"><rect x="16" y="14" width="18" height="22" rx="2" fill="none" stroke="#fff" stroke-width="2"/><path d="M20 22h10M20 27h10" stroke="#fff" stroke-width="2"/></svg></div>

  <div class="frame" style="left:111px;top:2231px;width:345px;height:347px"></div>
  <div class="photo" style="left:134px;top:2254px;width:392px;height:392px;background:linear-gradient(135deg,#1f2533 0%,#3c4355 45%,#6c6e78 70%,#1d2230 100%)" role="img" aria-label="Two colleagues smiling while reviewing a laptop together"></div>
  <div class="node" style="left:491px;top:2532px"><svg width="50" height="50"><rect x="14" y="18" width="22" height="16" rx="2" fill="none" stroke="#fff" stroke-width="2"/><path d="M20 18v-4h10v4" fill="none" stroke="#fff" stroke-width="2"/></svg></div>

  <h3 class="abs serif" style="left:637px;top:2282px;font-size:25px;font-weight:500">Business Law</h3>
  <div class="rule" style="left:637px;top:2322px;width:62px;height:3px"></div>
  <p class="para" style="left:637px;top:2358px;width:450px">Lorem ipsum dolor sit amet, consectetur adipiscing elit, sed do eiusmod tempor incididunt ut labore et dolore magna aliqua. Ut enim ad minim veniam, quis nostrud exercitat ion ullamco laboris nisi ut aliquip ex ea commo do consequat. Duis aute irure dolor in reprehenderit in voluptate velit esse cillum dolore eu fugiat nulla pariatur.</p>
  <div class="btn" style="left:637px;top:2559px;width:134px;height:44px">Learn More</div>
</section>

<!-- testimonials -->
<section>
  <div class="abs" style="left:0;top:2765px;width:1200px;height:534px;background:var(--navy)"></div>
  <h2 class="section-title" style="top:2842px;color:var(--white)">Our Testimonials</h2>
  <div class="rule" style="left:562px;top:2904px"></div>
  <div class="arrow" style="left:88px"><svg width="24" height="24"><path d="M17 12H7M11 8l-4 4 4 4" fill="none" stroke="#2d3562" stroke-width="2.2"/></svg></div>
  <div class="arrow" style="left:1087px"><svg width="24" height="24"><path d="M7 12h10M13 8l4 4-4 4" fill="none" stroke="#2d3562" stroke-width="2.2"/></svg></div>
  <article class="testi-card" style="left:171px">
    <div class="avatar" style="background:linear-gradient(135deg,#f4d6b8,#e29a5c)" role="img" aria-label="Client avatar"></div>
    <div class="name">Owen D.</div><div class="stars">★★★★★</div>
    <div class="role">Lorum Ipsum Dolor Sit Amet</div><div class="line"></div>
    <p class="quote">Marian is a true professional who is very knowledgeable in her field of expertise. She is extremely attentive to details and client concerns.</p>
  </article>
  <article class="testi-card" style="left:614px">
    <div class="avatar" style="background:linear-gradient(135deg,#eeeeee,#b8b8bd)" role="img" aria-label="Client avatar"></div>
    <div class="name">Theo K.</div><div class="stars">★★★★★</div>
    <div class="role">Lorum Ipsum Dolor Sit Amet</div><div class="line"></div>
    <p class="quote">Used Marian's services to create a long overdue will. She was awesome. Knowledgeable of all available products and provided great advice.</p>
  </article>
</section>

<!-- faq -->
<section>
  <h2 class="section-title" style="top:3374px">Frequently Asked Questions</h2>
  <div class="faq" style="top:3483px"><span>1. How can I learn more about Marian Thorpe?</span><i></i></div>
  <div class="faq" style="top:3549px"><span>2. How can I learn more about the Law Office of Marian J. Thorpe?</span><i></i></div>
  <div class="faq" style="top:3615px"><span>3.What can I expect from my Peace of Mind Planning Session?</span><i></i></div>
  <div class="faq" style="top:3681px"><span>4. What are the initial steps to get started?</span><i></i></div>
  <div class="faq open" style="top:3749px"><span>5. What kind of information do you need from me?</span><i></i>
    <p>Let me start by saying what we do NOT need! We do NOT need account statements, social security numbers, or tax returns. We DO need information on what kind of assets you own (house, retirement account, life insurance, etc.), their relative value, and how they are titled</p></div>
  <div class="btn" style="left:532px;top:3893px;width:134px;height:45px">View More</div>
</section>

<!-- news -->
<section>
  <h2 class="section-title" style="top:4104px">Our Latest News</h2>
  <div class="rule" style="left:562px;top:4166px"></div>
  <div class="photo" style="left:111px;top:4202px;width:339px;height:345px;background:linear-gradient(135deg,#c9d2dc 0%,#6b7a8c 45%,#2a3242 100%)" role="img" aria-label="Business team meeting in a bright office"></div>
  <div class="photo" style="left:478px;top:4202px;width:287px;height:184px;background:linear-gradient(135deg,#e5e7ea 0%,#8a9099 50%,#2a2f3b 100%)" role="img" aria-label="Attorney signing documents at a desk"></div>
  <h4 class="news-h" style="left:478px;top:4398px;width:290px">Lorem ipsum dolor sit amet, conse ctetur adipiscing</h4>
  <p class="news-p" style="left:478px;top:4456px;width:290px">Lorem ipsum dolor sit amet, consectetur a dipisci ng elit, sed do eiusmod tempor</p>
  <span class="news-link" style="left:478px;top:4514px">VIEW MORE</span>

  <h4 class="news-h" style="left:802px;top:4207px;width:290px">Lorem ipsum dolor sit amet, conse ctetur adipiscing</h4>
  <p class="news-p" style="left:802px;top:4263px;width:290px">Lorem ipsum dolor sit amet, consectetur a dipisci ng elit, sed do eiusmod tempor</p>
  <span class="news-link" style="left:802px;top:4318px">VIEW MORE</span>
  <h4 class="news-h" style="left:802px;top:4372px;width:290px">Lorem ipsum dolor sit amet, conse ctetur adipiscing</h4>
  <p class="news-p" style="left:802px;top:4428px;width:290px">Lorem ipsum dolor sit amet, consectetur a</p>
  <h4 class="news-h" style="left:802px;top:4485px;width:290px">Lorem ipsum dolor sit amet, conse ctetur adipiscing</h4>
  <p class="news-p" style="left:802px;top:4541px;width:290px">Lorem ipsum dolor sit amet, consectetur a</p>
  <div class="abs" style="left:1124px;top:4210px;width:3px;height:130px;background:#d8dae0"></div>
</section>

<!-- footer & cta -->
<footer>
  <div class="abs footer"></div>
  <div class="abs" style="left:969px;top:4644px;width:128px;height:111px;background:var(--navy)"></div>
  <div class="abs cta-box"></div>
  <h2 class="section-title" style="top:4700px;color:var(--white);font-size:40px">Book Your Free Call</h2>
  <p class="abs" style="left:240px;top:4788px;width:720px;text-align:center;font-size:14.5px;font-weight:600;line-height:31px;color:var(--white)">I'll meet you where you are. Whether you have questions or just need guidance, this call is a safe space to start.</p>
  <div class="btn" style="left:513px;top:4866px;width:174px;height:44px;background:var(--navy);font-size:11.5px">Schedule a Call</div>

  <div class="abs serif" style="left:0;top:5028px;width:1200px;text-align:center;font-size:22px;color:var(--white);letter-spacing:.5px">ATTORNEY MARIAN</div>
  <div class="abs" style="left:0;top:5070px;width:1200px;text-align:center;font-size:13px;font-weight:500;color:var(--white)">Legal Clarity for Life and Business</div>
  <nav class="fnav"><a href="#">HOME</a><a href="#">ABOUT</a><a href="#">SERVICES</a><a href="#">WHO I WORK WITH</a><a href="#">RESOURCES</a><a href="#">CONTACT US</a></nav>
  <div class="abs" style="left:270px;top:5172px;font-size:13.5px;font-weight:600;color:var(--white);display:flex;gap:7px;align-items:center">
    <svg width="12" height="12" viewBox="0 0 24 24"><path fill="#fff" d="M6.6 10.8a15.1 15.1 0 0 0 6.6 6.6l2.2-2.2c.3-.3.7-.4 1-.2 1.1.4 2.3.6 3.6.6.6 0 1 .4 1 1V20c0 .6-.4 1-1 1A17 17 0 0 1 3 4c0-.6.4-1 1-1h3.5c.6 0 1 .4 1 1 0 1.3.2 2.5.6 3.6.1.3 0 .7-.2 1z"/></svg>+1 (212) 555 0190</div>
  <div class="abs" style="left:478px;top:5172px;font-size:13.5px;font-weight:600;color:var(--white);display:flex;gap:7px;align-items:center">
    <svg width="13" height="11" viewBox="0 0 24 18"><path fill="#fff" d="M0 0h24v18H0z"/><path fill="none" stroke="#1c1c21" stroke-width="2" d="M1 1l11 9 11-9"/></svg>hello@attorneymarian.example</div>
  <div class="social" style="left:813px;top:5164px;width:32px;height:32px" aria-label="Social profile 1"></div>
  <div class="social" style="left:851px;top:5164px;width:32px;height:32px" aria-label="Social profile 2"></div>
  <div class="social" style="left:889px;top:5164px;width:32px;height:32px" aria-label="Social profile 3"></div>
  <div class="abs" style="left:0;top:5234px;width:1200px;text-align:center;font-size:10.5px;color:var(--white)">Copyright@2025 All Rights Reserved by attorney marian</div>
</footer>

</body>
</html>
```